Exciting New Reseller Brand requires Website to WOW New clients to register.

We are a NEW online business called Trade Our Goods.

The Website is a simple concept, it looks to put Merchants (businesses that want their products resold) in touch with Resellers (people or businesses that want to resell that product).

The website acts as an online market place which looks to get Merchants to sign-up and pay to list their company and product as well as getting Resellers to sign-up to view potential Merchants they can get in touch with in the right industry or area to resell their products for (see attached slide-pack to explain packages)

Any type of Industry or Business can register themselves to get listed on Trade Our Goods to see either get their product/service resold or to look for products / services to reseller.

Trade Our Goods does not take any other monetary part in the business relationships other than to obtain money for the monthly website subscription.

We want a very simple website, so this project is for several pages:

Page 1) A really vibrant, exciting, image based homepage to get people to sign-up / register (see sites that we like in the project brief). Needs to be very clear that there are 2 customers and to sign up to join, build and earn!

Page 2) A page that describes the benefits and packages for Resellers.

Page 3) A page that describes the benefits and packages for Merchants.

Page 4) The Payment process pages, taking the customer through sign-up

Page 5) The Business Listings page, so when people search for a Merchant how this will be displayed.

We would really like an image based site and preferably parallax. We want it bright vibrant and to look like a social media site.

All necessary files / logos enclosed.

We would love to continue to work with the winning designer moving forward.

Many thanks and Good Luck.

Regards

Martin & Owen

Target Market(s)

Merchants, Suppliers, Vendors, Manufacturers, Distributors, Wholesalers, Affiliate programs, Franchisees, Reselers

Industry/Entity Type

Business

Number of Pages Required

5+ page

Requirements
Must have
• We love the following websites:
• 1) Like the top section, i.e. parallax image based: www.brightkitestudio.co.uk
• 2) Like the way the screen is split in 2, could be used to describe the 2 different customers we are after Merchants / Resellers: www.filevault-example.com/guide
• 3) Like the bright colours / full screen video split into 2 below top banner and the generally how simple the site is: www.harbourlinden.com.au
• 4) Love all of this site, simple, bold, Love the colours, the clear message and the infographics: http://www.velorin-example.com/swiftrider/faster

```html
<!DOCTYPE html>
<html lang="en">
<head>
<meta charset="utf-8">
<title>Trade Our Goods – Home</title>
<link href="https://fonts.googleapis.com/css2?family=Open+Sans:wght@300;400;600;700;800&display=swap" rel="stylesheet">
<style>
:root{
  --blue:#1f8fd6;
  --blue-dark:#1776b8;
  --green:#8cc63f;
  --green-dark:#76ad2e;
  --ink:#2d3138;
  --muted:#6b7178;
  --line:#e3e6ea;
  --panel:#f1f3f5;
  --tier-head:#3b4049;
  --footer:#202328;
  --white:#ffffff;
}
*{box-sizing:border-box;margin:0;padding:0}
html,body{width:1200px;height:3620px;overflow:hidden}
body{font-family:"Open Sans",Arial,sans-serif;color:var(--ink);background:var(--white);position:relative}
section,header,footer{position:absolute;left:0;width:1200px}

/* hero */
.hero{top:0;height:740px;overflow:hidden}
.hero-photo{position:absolute;inset:0;background:linear-gradient(180deg,#3a3f46 0%,#55595f 45%,#2b2e33 100%)}
.nav{position:absolute;top:0;left:0;width:1200px;height:72px;display:flex;align-items:center;padding:0 40px 0 60px;background:rgba(20,22,26,.35)}
.brand{display:flex;align-items:center;gap:10px;font-weight:700;font-size:22px;color:var(--white)}
.brand-dot{width:30px;height:30px;border-radius:50%;background:var(--green)}
.nav ul{list-style:none;display:flex;margin-left:auto;gap:6px}
.nav li{font-size:13px;font-weight:600;color:var(--white);padding:9px 16px;letter-spacing:.5px}
.nav li.active{border:1px solid var(--white)}
.hero-copy{position:absolute;top:300px;left:0;width:1200px;text-align:center;color:var(--white)}
.hero-copy .lead{font-size:34px;font-weight:600}
.hero-copy h1{font-size:58px;font-weight:700;line-height:1.1;margin-top:4px}
.hero-copy .tag{font-size:14px;letter-spacing:3px;margin-top:18px}
.btn-outline{display:inline-block;border:1px solid var(--white);color:var(--white);font-size:13px;font-weight:600;padding:10px 26px;margin-top:22px;letter-spacing:1px}
.slide-arrow{position:absolute;top:380px;width:22px;height:34px}
.slide-arrow.prev{left:20px}.slide-arrow.next{right:20px}

/* why */
.why{top:740px;height:372px}
.why-text{position:absolute;left:100px;top:40px;width:500px}
.eyebrow{font-size:28px;font-weight:800;letter-spacing:1px}
.eyebrow .hl{color:var(--green)}
.sub{font-size:26px;font-weight:600;margin-top:14px;color:var(--ink)}
.masses{font-size:46px;font-weight:800;color:var(--blue);line-height:1.05}
.ticks{list-style:none;margin-top:16px}
.ticks li{font-size:14px;color:var(--muted);display:flex;align-items:center;gap:12px;line-height:26px}
.ticks svg{flex:none}
.why-photo{position:absolute;left:620px;top:30px;width:500px;height:330px;background:linear-gradient(180deg,#e9f3fb,#b9d9f1)}

/* split */
.split{top:1112px;height:408px;display:flex}
.split-half{width:600px;height:408px;padding:56px 70px 0;color:var(--white);text-align:center}
.split-half.merchants{background:var(--blue)}
.split-half.resellers{background:var(--green)}
.split-half h2{font-size:50px;font-weight:400;letter-spacing:1px}
.split-half h3{font-size:22px;font-weight:600;color:#16324a;margin-top:2px}
.split-half.resellers h3{color:#2e4414}
.split-half p{font-size:14px;line-height:22px;margin-top:18px}
.btn-light{display:inline-flex;align-items:center;gap:8px;background:var(--white);color:var(--blue);font-size:13px;font-weight:700;padding:10px 20px;margin-top:28px;border:2px solid rgba(255,255,255,.6)}
.resellers .btn-light{color:var(--green-dark)}

/* how it works */
.how{top:1520px;height:560px}
.how-screen{position:absolute;left:140px;top:80px;width:420px;height:380px;background:linear-gradient(160deg,#3d2a6b,#1c6fb8 55%,#c7cbd1 85%)}
.how-text{position:absolute;left:620px;top:150px;width:480px}
.how-text h2{font-size:28px;font-weight:800;letter-spacing:1px}

/* pricing */
.pricing{top:2080px;height:480px;background:var(--panel)}
.price-intro{position:absolute;left:100px;top:70px;width:240px;text-align:right}
.price-intro h2{font-size:42px;font-weight:800;line-height:1}
.price-intro h3{font-size:24px;font-weight:400;color:var(--muted)}
.feature-list{position:absolute;left:100px;top:205px;width:240px;list-style:none;text-align:right}
.feature-list li,.tier li{height:40px;line-height:40px;font-size:14px;color:var(--muted);border-bottom:1px solid var(--line)}
.btn-green{display:inline-block;background:var(--green);color:var(--white);font-size:13px;font-weight:700;padding:11px 24px;letter-spacing:.5px}
.feature-btn{position:absolute;left:228px;top:420px}
.tier{position:absolute;top:110px;width:200px;background:var(--white)}
.tier.t1{left:370px}.tier.t2{left:620px}.tier.t3{left:870px}
.tier-head{background:var(--tier-head);color:var(--white);text-align:center;font-size:18px;font-weight:600;height:52px;line-height:52px}
.tier-price{background:var(--green);color:var(--white);text-align:center;height:52px;line-height:52px;font-size:15px}
.tier-price b{font-size:30px;font-weight:700}
.tier ul{list-style:none}
.tier li{text-align:center;display:flex;align-items:center;justify-content:center}
.tier-foot{text-align:center;padding:18px 0}

/* benefits */
.benefits{top:2560px;height:400px}
.benefits h2{text-align:center;font-size:32px;font-weight:600;letter-spacing:1px;margin-top:50px}
.benefits h2 .hl{color:var(--green)}
.benefit-col{position:absolute;top:130px;width:300px}
.benefit-col h3{font-size:36px;font-weight:600}
.benefit-col.merchants{left:100px}
.benefit-col.merchants h3{color:var(--blue)}
.benefit-col.resellers{left:820px}
.benefit-col.resellers h3{color:var(--green)}
.benefit-col ul{list-style:none;margin-top:12px}
.benefit-col li{font-size:14px;color:var(--muted);line-height:26px}
.benefit-col.merchants li{text-align:right;padding-right:30px}
.benefits-photo{position:absolute;left:470px;top:130px;width:260px;height:250px;background:radial-gradient(ellipse at 50% 40%,#9bd15a 0%,#c9a64a 60%,#f4f1e6 100%)}

/* footer */
.site-footer{top:2960px;height:592px;background:var(--footer);color:#c7cbd1;text-align:center}
.footer-brand{display:flex;justify-content:center;align-items:center;gap:14px;margin-top:60px;font-size:36px;font-weight:700;color:var(--white)}
.footer-brand .brand-dot{width:46px;height:46px}
.contact{list-style:none;margin-top:26px;font-size:14px;line-height:26px}
.contact li{display:flex;justify-content:center;align-items:center;gap:8px}
.contact-form{position:absolute;left:310px;top:360px;width:580px;display:flex;gap:20px;text-align:left}
.form-left{width:250px}
.field{display:flex;align-items:center;height:36px;border:1px solid #4a4f57;margin-bottom:12px;padding:0 10px;font-size:13px;color:#9aa0a7}
.message{flex:1;height:132px;border:1px solid #4a4f57;padding:8px 10px;font-size:13px;color:#9aa0a7}
.submit{position:absolute;left:590px;top:510px;width:310px;background:var(--blue);color:var(--white);font-size:13px;font-weight:700;text-align:center;height:34px;line-height:34px}

.bottom-bar{top:3552px;height:68px;background:var(--blue-dark);color:var(--white);display:flex;align-items:center;padding:0 60px;font-size:13px}
.social{margin-left:auto;display:flex;align-items:center;gap:10px}
.social span{width:24px;height:24px;border-radius:50%;background:var(--white);display:inline-block}
</style>
</head>
<body>

<header class="hero">
  <div class="hero-photo" role="img" aria-label="Dark business photo of silhouetted people standing on rising bar columns with a red growth arrow"></div>
  <nav class="nav">
    <div class="brand"><span class="brand-dot"></span>Trade Our Goods</div>
    <ul>
      <li>HOME</li><li>ABOUT US</li><li>PRODUCT</li><li>RESELLERS</li><li>HOW IT WORKS</li><li class="active">CONTACT US</li>
    </ul>
  </nav>
  <div class="hero-copy">
    <p class="lead">Building your own</p>
    <h1>Virtual Sales Team</h1>
    <p class="tag">JOIN | BUILD | EARN</p>
    <span class="btn-outline">OUR PRODUCTS</span>
  </div>
  <svg class="slide-arrow prev" viewBox="0 0 22 34"><path d="M16 4 5 17l11 13" fill="none" stroke="#fff" stroke-width="3"/></svg>
  <svg class="slide-arrow next" viewBox="0 0 22 34"><path d="M6 4l11 13L6 30" fill="none" stroke="#fff" stroke-width="3"/></svg>
</header>

<section class="why">
  <div class="why-text">
    <h2 class="eyebrow">WHY PICK <span class="hl">RESELLING</span></h2>
    <p class="sub">Bringing Reseller Opportunities</p>
    <p class="masses">TO THE MASSES</p>
    <ul class="ticks">
      <li><svg width="14" height="14" viewBox="0 0 14 14"><path d="M2 7l3 3 7-7" fill="none" stroke="#1f8fd6" stroke-width="2"/></svg>Personal requirement for a reseller base</li>
      <li><svg width="14" height="14" viewBox="0 0 14 14"><path d="M2 7l3 3 7-7" fill="none" stroke="#1f8fd6" stroke-width="2"/></svg>Experienced reseller models that work</li>
      <li><svg width="14" height="14" viewBox="0 0 14 14"><path d="M2 7l3 3 7-7" fill="none" stroke="#1f8fd6" stroke-width="2"/></svg>Building an effective virtual sales team</li>
      <li><svg width="14" height="14" viewBox="0 0 14 14"><path d="M2 7l3 3 7-7" fill="none" stroke="#1f8fd6" stroke-width="2"/></svg>Helping SME's earn money for old rope</li>
      <li><svg width="14" height="14" viewBox="0 0 14 14"><path d="M2 7l3 3 7-7" fill="none" stroke="#1f8fd6" stroke-width="2"/></svg>Easy to generate revenue for a minimal cost</li>
    </ul>
  </div>
  <div class="why-photo" role="img" aria-label="Illustration of business people shaking hands in blue and green silhouettes"></div>
</section>

<section class="split">
  <div class="split-half merchants">
    <h2>MERCHANTS</h2>
    <h3>Grow Business &amp; Increase Sales</h3>
    <p>Reach a ready network of resellers who want to sell what you make. List your products, set your terms and let a growing sales team carry your brand into new markets across every region.</p>
    <span class="btn-light">GET STARTED <svg width="12" height="12" viewBox="0 0 12 12"><path d="M2 6h8M7 3l3 3-3 3" fill="none" stroke="currentColor" stroke-width="2"/></svg></span>
  </div>
  <div class="split-half resellers">
    <h2>RESELLERS</h2>
    <h3>Grow Portfolio &amp; Increase Income</h3>
    <p>Find merchants in your industry and area with products ready to resell. Add new lines to your portfolio, build lasting partnerships and increase your income with no stock and no upfront costs.</p>
    <span class="btn-light">GET STARTED <svg width="12" height="12" viewBox="0 0 12 12"><path d="M2 6h8M7 3l3 3-3 3" fill="none" stroke="currentColor" stroke-width="2"/></svg></span>
  </div>
</section>

<section class="how">
  <div class="how-screen" role="img" aria-label="Desktop computer showing the marketplace website"></div>
  <div class="how-text">
    <h2>HOW IT WORKS</h2>
    <p class="sub">Bringing Reseller Opportunities</p>
    <p class="masses">TO THE MASSES</p>
    <ul class="ticks">
      <li><svg width="14" height="14" viewBox="0 0 14 14"><path d="M2 7l3 3 7-7" fill="none" stroke="#1f8fd6" stroke-width="2"/></svg>Portal for Resellers and Merchants</li>
      <li><svg width="14" height="14" viewBox="0 0 14 14"><path d="M2 7l3 3 7-7" fill="none" stroke="#1f8fd6" stroke-width="2"/></svg>Merchants can promote their products</li>
      <li><svg width="14" height="14" viewBox="0 0 14 14"><path d="M2 7l3 3 7-7" fill="none" stroke="#1f8fd6" stroke-width="2"/></svg>Merchants can build a virtual sales team</li>
      <li><svg width="14" height="14" viewBox="0 0 14 14"><path d="M2 7l3 3 7-7" fill="none" stroke="#1f8fd6" stroke-width="2"/></svg>Resellers can expand product portfolio</li>
      <li><svg width="14" height="14" viewBox="0 0 14 14"><path d="M2 7l3 3 7-7" fill="none" stroke="#1f8fd6" stroke-width="2"/></svg>Resellers can generate revenue</li>
      <li><svg width="14" height="14" viewBox="0 0 14 14"><path d="M2 7l3 3 7-7" fill="none" stroke="#1f8fd6" stroke-width="2"/></svg>Industry news and opportunities</li>
    </ul>
  </div>
</section>

<section class="pricing">
  <div class="price-intro">
    <h2>PRODUCT</h2>
    <h3>Price Structure</h3>
  </div>
  <ul class="feature-list">
    <li>Search Merchant Database</li>
    <li>Reseller Listing</li>
    <li>Monthly Newsletters</li>
    <li>Seminars &amp; Network Events</li>
    <li>Dedicated Merchant Group</li>
  </ul>
  <span class="btn-green feature-btn">RESELLERS</span>

  <div class="tier t1">
    <div class="tier-head">TIER 1</div>
    <div class="tier-price"><b>£25</b>.00 p/month</div>
    <ul>
      <li><svg width="16" height="16" viewBox="0 0 16 16"><path d="M2 8l4 4 8-8" fill="none" stroke="#8cc63f" stroke-width="2.5"/></svg></li>
      <li></li><li></li><li></li><li></li>
    </ul>
    <div class="tier-foot"><span class="btn-green">GET STARTED</span></div>
  </div>
  <div class="tier t2">
    <div class="tier-head">TIER 2</div>
    <div class="tier-price"><b>£25</b>.00 p/month</div>
    <ul>
      <li><svg width="16" height="16" viewBox="0 0 16 16"><path d="M2 8l4 4 8-8" fill="none" stroke="#8cc63f" stroke-width="2.5"/></svg></li>
      <li><svg width="16" height="16" viewBox="0 0 16 16"><path d="M2 8l4 4 8-8" fill="none" stroke="#8cc63f" stroke-width="2.5"/></svg></li>
      <li><svg width="16" height="16" viewBox="0 0 16 16"><path d="M2 8l4 4 8-8" fill="none" stroke="#8cc63f" stroke-width="2.5"/></svg></li>
      <li></li><li></li>
    </ul>
    <div class="tier-foot"><span class="btn-green">GET STARTED</span></div>
  </div>
  <div class="tier t3">
    <div class="tier-head">TIER 3</div>
    <div class="tier-price"><b>£25</b>.00 p/month</div>
    <ul>
      <li><svg width="16" height="16" viewBox="0 0 16 16"><path d="M2 8l4 4 8-8" fill="none" stroke="#8cc63f" stroke-width="2.5"/></svg></li>
      <li><svg width="16" height="16" viewBox="0 0 16 16"><path d="M2 8l4 4 8-8" fill="none" stroke="#8cc63f" stroke-width="2.5"/></svg></li>
      <li><svg width="16" height="16" viewBox="0 0 16 16"><path d="M2 8l4 4 8-8" fill="none" stroke="#8cc63f" stroke-width="2.5"/></svg></li>
      <li><svg width="16" height="16" viewBox="0 0 16 16"><path d="M2 8l4 4 8-8" fill="none" stroke="#8cc63f" stroke-width="2.5"/></svg></li>
      <li><svg width="16" height="16" viewBox="0 0 16 16"><path d="M2 8l4 4 8-8" fill="none" stroke="#8cc63f" stroke-width="2.5"/></svg></li>
    </ul>
    <div class="tier-foot"><span class="btn-green">GET STARTED</span></div>
  </div>
</section>

<section class="benefits">
  <h2>BENEFITS <span class="hl">FOR</span> EVERYONE</h2>
  <div class="benefit-col merchants">
    <h3>Merchants</h3>
    <ul>
      <li>Additional Source of Sales</li>
      <li>Incremental Growth</li>
      <li>Viral Brand Management</li>
      <li>Virtual Sales Team</li>
      <li>No Overheads</li>
    </ul>
  </div>
  <div class="benefits-photo" role="img" aria-label="Young green plant growing from a pile of gold coins"></div>
  <div class="benefit-col resellers">
    <h3>Resellers</h3>
    <ul>
      <li>Additional Stream of Income</li>
      <li>Infrastructure in Place</li>
      <li>No Additional Cost</li>
      <li>Expand Product Suite</li>
      <li>Reach New Target Markets</li>
    </ul>
  </div>
</section>

<footer class="site-footer">
  <div class="footer-brand"><span class="brand-dot"></span>Trade Our Goods</div>
  <ul class="contact">
    <li><svg width="12" height="14" viewBox="0 0 12 14"><path d="M6 1a4 4 0 0 1 4 4c0 3-4 8-4 8S2 8 2 5a4 4 0 0 1 4-4z" fill="#c7cbd1"/></svg>12 Harbour Row, Eastfield, Northland</li>
    <li><svg width="12" height="12" viewBox="0 0 12 12"><path d="M2 1h3l1 3-2 1a7 7 0 0 0 3 3l1-2 3 1v3c-6 0-9-3-9-9z" fill="#c7cbd1"/></svg>(010) 555 2718 &nbsp;|&nbsp; (010) 555 4096</li>
    <li><svg width="14" height="10" viewBox="0 0 14 10"><rect x="0.5" y="0.5" width="13" height="9" fill="none" stroke="#c7cbd1"/><path d="M1 1l6 5 6-5" fill="none" stroke="#c7cbd1"/></svg>office@tradeourgoods.com</li>
  </ul>
  <div class="contact-form">
    <div class="form-left">
      <div class="field">Name:</div>
      <div class="field">Email:</div>
      <div class="field">Phone:</div>
    </div>
    <div class="message">Message:</div>
  </div>
  <div class="submit">SUBMIT</div>
</footer>

<div class="bottom-bar" style="position:absolute;left:0;top:3552px;width:1200px;height:68px">
  <span>Trade Our Goods © 2015. All Rights Reserved</span>
  <div class="social">Connect with our social networks <span></span><span></span><span></span></div>
</div>

</body>
</html>
```